Feedback App to request feedback from colleagues

It’s a small web app to collect feedback from team members. This is the general screen flow but happy for variations to it.

Users logs into application and is able to see the feedback received till date from different colleagues.

At the top right are “Request feedback”, “Respond to Feedback”.

When the user clicks on Request Feedback, there are three options.
Adhoc Feedback
Mid Year Feedback
360 Feedback

Adhoc feedback will open a screen where I can search for colleagues to request feedback from (I can select more than one). There are three pre-defined question that can I edit if needed.

Mid year feedback: same process but questions cannot be edited

360 Feedback - just redirect to another website.

Respond to Feedback - see incoming request and the ability to provide feedback to questions received.

Send Feedback: select a colleague and send adhoc feedback.

Colours to be used are white and red only. Simple design, the app will be embedded in a portal so need for headers etc. think of a mobile view but no need for logo, header bar etc

Colour Codes:
Red: #E60000
White #FFFFFF
Grey: #333333 (Only use if needed e.g. borders, background etc)
Black: #000000

Only the above colours to be used

Number of Pages Required

1 page

Font styles to use
Sans Serif

Colors
EB3D1F
EC4F4E
F09395
F8D3D4
FCEDEE

Requirements
Must have
• Design screens for every page mentioned
Nice to have
• Clean design, use of images and icons
Should not have
• Cluttered design, header

```html
<!DOCTYPE html>
<html lang="en">
<head>
<meta charset="utf-8">
<title>Feedback App Screens</title>
<link href="https://fonts.googleapis.com/css2?family=Montserrat:wght@500;600;700;800&family=Mulish:wght@400;500;600&display=swap" rel="stylesheet">
<style>
:root{
  --stage:#808185;
  --red:#E02A2A;
  --red-dark:#D42020;
  --red-soft:#EC4F4E;
  --white:#FFFFFF;
  --surface:#F4F4F5;
  --ink:#111111;
  --text:#555555;
  --muted:#9A9A9A;
  --line:#D2D2D2;
  --star-off:#CFCFCF;
  --ok:#2FB344;
}
*{box-sizing:border-box;margin:0;padding:0}
html,body{width:709px;height:1200px;overflow:hidden;background:var(--stage)}
.canvas{position:relative;width:709px;height:1200px;overflow:hidden;background:var(--stage)}
.screen{position:absolute;width:647px;background:var(--surface);transform-origin:0 0;transform:scale(.4778);font-family:"Mulish",sans-serif;color:var(--ink);overflow:hidden}
.screen-list-a{left:35.8px;top:31.1px;height:1624px}
.screen-list-b{left:357.4px;top:27.2px;height:1632px}
.screen-adhoc{left:199.7px;top:828px;height:688px}

.screen-head{position:absolute;left:0;top:0;width:100%;background:var(--white)}
.screen-list-a .screen-head{height:83px}
.screen-list-b .screen-head,.screen-adhoc .screen-head{height:91px}
.screen-adhoc .screen-head{height:71px}
.page-title{position:absolute;left:69px;font-family:"Montserrat",sans-serif;font-weight:800;font-size:12.5px;letter-spacing:.1px;color:var(--ink)}
.page-title::after{content:"";position:absolute;left:1px;top:27px;width:133px;height:1px;background:var(--muted)}
.screen-adhoc .page-title{font-size:13.5px;letter-spacing:.6px}
.screen-adhoc .page-title::after{width:127px;top:26px}

.btn{position:absolute;height:27px;width:107px;display:flex;align-items:center;justify-content:center;font-family:"Montserrat",sans-serif;font-weight:600;font-size:7.2px;border:1px solid var(--red);color:var(--red);background:var(--white)}
.btn-solid{background:var(--red);color:var(--white)}
.btn-caret{position:absolute;left:50%;bottom:-6px;margin-left:-4px;width:0;height:0;border-left:4px solid transparent;border-right:4px solid transparent;border-top:6px solid var(--red)}

.request-menu{position:absolute;left:300px;top:65px;height:26px;display:flex}
.request-menu span{display:flex;align-items:center;justify-content:center;height:26px;background:var(--red-soft);color:var(--white);font-family:"Montserrat",sans-serif;font-weight:600;font-size:7.2px;border-left:1px solid rgba(255,255,255,.35)}
.request-menu .menu-active{background:var(--red-dark);border-left:0}

.toolbar{position:absolute;left:0;width:100%;height:18px}
.sort-label{position:absolute;left:71px;top:5px;font-family:"Montserrat",sans-serif;font-weight:600;font-size:6px}
.select{position:absolute;top:0;height:18px;border:1px solid var(--line);background:var(--white);font-size:5.6px;color:#444;display:flex;align-items:center;padding-left:6px}
.select svg{position:absolute;right:6px;top:6px}
.pager{position:absolute;display:flex;align-items:center;gap:6px}
.pager .page{width:14px;height:14px;border:1px solid var(--line);background:var(--white);display:flex;align-items:center;justify-content:center;font-size:6.5px;color:#444}
.pager .page-on{background:var(--red);border-color:var(--red);color:var(--white)}
.pager .arrow{width:10px;height:14px;display:flex;align-items:center;justify-content:center}

.feed{position:absolute;left:71px;width:504px;display:flex;flex-direction:column;gap:12px}
.card{position:relative;height:130px;background:var(--white);box-shadow:0 1px 2px rgba(0,0,0,.06)}
.avatar{position:absolute;border-radius:50%}
.card .avatar{left:19px;top:20px;width:44px;height:44px}
.av-tan{background:radial-gradient(circle at 50% 40%,#b08d74,#d9cfc6 70%)}
.av-grey{background:radial-gradient(circle at 50% 40%,#8a7a70,#6f6f73 70%)}
.av-maroon{background:radial-gradient(circle at 50% 35%,#a0705a,#8d1d2c 65%)}
.av-slate{background:radial-gradient(circle at 50% 40%,#9a8777,#4f6f95 60%,#dfe3e8 75%)}
.av-sky{background:radial-gradient(circle at 50% 35%,#8d6a55,#e8a22a 55%,#8ccbe6 72%)}
.card-title{position:absolute;left:77px;top:17px;font-family:"Montserrat",sans-serif;font-weight:600;font-size:7.8px;color:var(--red)}
.stars{position:absolute;left:77px;top:30px;font-size:8.5px;letter-spacing:.6px;color:var(--red);line-height:1}
.stars .off{color:var(--star-off)}
.card-text{position:absolute;left:77px;top:52px;width:410px;font-size:6.2px;line-height:10.4px;color:var(--text)}
.card-meta{position:absolute;left:76px;top:104px;display:flex;align-items:center;font-size:5.6px;color:#444}
.card-meta .who{font-family:"Montserrat",sans-serif;font-weight:600;font-size:6.3px;color:var(--ink);margin-right:8px}
.card-meta svg{margin-right:3px}
.card-meta .where{margin-right:10px}

.search{position:absolute;left:207px;top:92px;width:234px;height:27px;background:var(--white);border:1px solid var(--line);font-size:6.5px;color:#333;display:flex;align-items:center;padding-left:11px}
.search svg{position:absolute;right:11px;top:9px}
.people{position:absolute;left:72px;top:138px;width:504px;height:515px;background:var(--white)}
.person{position:absolute;left:0;width:504px;height:44px;border-top:1px solid #ECECEC}
.person .avatar{left:15px;top:9px;width:26px;height:26px}
.person-name{position:absolute;left:53px;top:17px;font-family:"Montserrat",sans-serif;font-weight:600;font-size:6.8px}
.person-btn{position:absolute;left:402px;top:11px;width:84px;height:21px;background:#F1F1F1;color:var(--muted);font-size:6.2px;display:flex;align-items:center;justify-content:center}
.person-first{border-top:0;height:125px}
.person-first .avatar{top:14px}
.person-first .person-name{top:22px}
.person-first .person-btn{top:18px;background:var(--red);color:var(--white);font-family:"Montserrat",sans-serif;font-weight:600}
.picked{position:absolute;left:35px;top:15px;width:10px;height:10px;border-radius:50%;background:var(--ok);border:1.5px solid var(--white)}
.questions{position:absolute;left:51px;top:46px;width:435px;height:65px;background:#F4F4F5;padding:12px 0 0 14px}
.questions p{font-size:6.2px;color:#333;text-decoration:underline;line-height:16px;display:flex;align-items:center}
.questions svg{margin-left:6px}
</style>
</head>
<body>
<div class="canvas">

  <!-- Feedback list screen -->
  <section class="screen screen-list-a">
    <header class="screen-head">
      <h1 class="page-title" style="top:27px">LIST OF FEEDBACKS</h1>
      <a class="btn" style="left:351px;top:26px">Request Feedback</a>
      <a class="btn" style="left:468px;top:26px">Respond to Feedback</a>
    </header>
    <div class="toolbar" style="top:104px">
      <span class="sort-label">Sort By</span>
      <span class="select" style="left:109px;width:47px">Newest<svg width="6" height="4" viewBox="0 0 6 4"><path d="M.5.5 3 3 5.5.5" fill="none" stroke="#444" stroke-width=".8"/></svg></span>
      <span class="select" style="left:162px;width:58px">Date Range<svg width="6" height="4" viewBox="0 0 6 4"><path d="M.5.5 3 3 5.5.5" fill="none" stroke="#444" stroke-width=".8"/></svg></span>
      <span class="select" style="left:226px;width:57px">Very Good<svg width="6" height="4" viewBox="0 0 6 4"><path d="M.5.5 3 3 5.5.5" fill="none" stroke="#444" stroke-width=".8"/></svg></span>
      <div class="pager" style="left:439px;top:2px">
        <span class="arrow"><svg width="5" height="9" viewBox="0 0 5 9"><path d="M4.5.5 .5 4.5l4 4" fill="none" stroke="#999"/></svg></span>
        <span class="page page-on">1</span><span class="page">2</span><span class="page">3</span><span class="page">4</span><span class="page">5</span>
        <span class="arrow"><svg width="5" height="9" viewBox="0 0 5 9"><path d="M.5.5l4 4-4 4" fill="none" stroke="#999"/></svg></span>
      </div>
    </div>
    <div class="feed" style="top:143px">
      <article class="card"><div class="avatar av-tan" role="img" aria-label="Colleague portrait photo"></div><h2 class="card-title">Good Quality</h2><div class="stars">★★★★★</div><p class="card-text">Lorem ipsum dolor sit amet, consectetur adipiscing elit, sed do eiusmod tempor incididunt ut labore et dolore magna aliqua. Ut enim ad minim veniam, quis nostrud exercitation ullamco laboris nisi ut aliquip ex ea commodo consequat. Duis aute irure dolor in reprehenderit in voluptate velit esse cillum dolore eu fugiat nulla pariatur. Excepteur sint occaecat cupidatat non proident, sunt in culpa qui officia deserunt mollit anim id est laborum</p><div class="card-meta"><span class="who">Owen Pratt</span><svg width="5" height="7" viewBox="0 0 5 7"><path d="M2.5 6.5S.5 4.3.5 2.6a2 2 0 0 1 4 0c0 1.7-2 3.9-2 3.9z" fill="none" stroke="#444" stroke-width=".6"/><circle cx="2.5" cy="2.6" r=".7" fill="#444"/></svg><span class="where">London</span><svg width="7" height="7" viewBox="0 0 7 7"><rect x=".5" y="1" width="6" height="5.5" fill="none" stroke="#444" stroke-width=".6"/><path d="M.5 2.6h6M2 .3v1.4M5 .3v1.4" stroke="#444" stroke-width=".6"/></svg><span>April 2, 2024</span></div></article>
      <article class="card"><div class="avatar av-grey" role="img" aria-label="Colleague portrait photo"></div><h2 class="card-title">Poor</h2><div class="stars"><span class="off">★★★★★</span></div><p class="card-text">Lorem ipsum dolor sit amet, consectetur adipiscing elit, sed do eiusmod tempor incididunt ut labore et dolore magna aliqua. Ut enim ad minim veniam, quis nostrud exercitation ullamco laboris nisi ut aliquip ex ea commodo consequat. Duis aute irure dolor in reprehenderit in voluptate velit esse cillum dolore eu fugiat nulla pariatur. Excepteur sint occaecat cupidatat non proident, sunt in culpa qui officia deserunt mollit anim id est laborum</p><div class="card-meta"><span class="who">Owen Pratt</span><svg width="5" height="7" viewBox="0 0 5 7"><path d="M2.5 6.5S.5 4.3.5 2.6a2 2 0 0 1 4 0c0 1.7-2 3.9-2 3.9z" fill="none" stroke="#444" stroke-width=".6"/><circle cx="2.5" cy="2.6" r=".7" fill="#444"/></svg><span class="where">London</span><svg width="7" height="7" viewBox="0 0 7 7"><rect x=".5" y="1" width="6" height="5.5" fill="none" stroke="#444" stroke-width=".6"/><path d="M.5 2.6h6M2 .3v1.4M5 .3v1.4" stroke="#444" stroke-width=".6"/></svg><span>April 2, 2024</span></div></article>
      <article class="card"><div class="avatar av-maroon" role="img" aria-label="Colleague portrait photo"></div><h2 class="card-title">Outstanding Performance</h2><div class="stars">★★★★★</div><p class="card-text">Lorem ipsum dolor sit amet, consectetur adipiscing elit, sed do eiusmod tempor incididunt ut labore et dolore magna aliqua. Ut enim ad minim veniam, quis nostrud exercitation ullamco laboris nisi ut aliquip ex ea commodo consequat. Duis aute irure dolor in reprehenderit in voluptate velit esse cillum dolore eu fugiat nulla pariatur. Excepteur sint occaecat cupidatat non proident, sunt in culpa qui officia deserunt mollit anim id est laborum</p><div class="card-meta"><span class="who">Owen Pratt</span><svg width="5" height="7" viewBox="0 0 5 7"><path d="M2.5 6.5S.5 4.3.5 2.6a2 2 0 0 1 4 0c0 1.7-2 3.9-2 3.9z" fill="none" stroke="#444" stroke-width=".6"/><circle cx="2.5" cy="2.6" r=".7" fill="#444"/></svg><span class="where">London</span><svg width="7" height="7" viewBox="0 0 7 7"><rect x=".5" y="1" width="6" height="5.5" fill="none" stroke="#444" stroke-width=".6"/><path d="M.5 2.6h6M2 .3v1.4M5 .3v1.4" stroke="#444" stroke-width=".6"/></svg><span>April 2, 2024</span></div></article>
      <article class="card"><div class="avatar av-slate" role="img" aria-label="Colleague portrait photo"></div><h2 class="card-title">High-Quality Work</h2><div class="stars">★★★★★</div><p class="card-text">Lorem ipsum dolor sit amet, consectetur adipiscing elit, sed do eiusmod tempor incididunt ut labore et dolore magna aliqua. Ut enim ad minim veniam, quis nostrud exercitation ullamco laboris nisi ut aliquip ex ea commodo consequat. Duis aute irure dolor in reprehenderit in voluptate velit esse cillum dolore eu fugiat nulla pariatur. Excepteur sint occaecat cupidatat non proident, sunt in culpa qui officia deserunt mollit anim id est laborum</p><div class="card-meta"><span class="who">Owen Pratt</span><svg width="5" height="7" viewBox="0 0 5 7"><path d="M2.5 6.5S.5 4.3.5 2.6a2 2 0 0 1 4 0c0 1.7-2 3.9-2 3.9z" fill="none" stroke="#444" stroke-width=".6"/><circle cx="2.5" cy="2.6" r=".7" fill="#444"/></svg><span class="where">London</span><svg width="7" height="7" viewBox="0 0 7 7"><rect x=".5" y="1" width="6" height="5.5" fill="none" stroke="#444" stroke-width=".6"/><path d="M.5 2.6h6M2 .3v1.4M5 .3v1.4" stroke="#444" stroke-width=".6"/></svg><span>April 2, 2024</span></div></article>
      <article class="card"><div class="avatar av-sky" role="img" aria-label="Colleague portrait photo"></div><h2 class="card-title">Needs Improvement</h2><div class="stars">★★★<span class="off">★★</span></div><p class="card-text">Lorem ipsum dolor sit amet, consectetur adipiscing elit, sed do eiusmod tempor incididunt ut labore et dolore magna aliqua. Ut enim ad minim veniam, quis nostrud exercitation ullamco laboris nisi ut aliquip ex ea commodo consequat. Duis aute irure dolor in reprehenderit in voluptate velit esse cillum dolore eu fugiat nulla pariatur. Excepteur sint occaecat cupidatat non proident, sunt in culpa qui officia deserunt mollit anim id est laborum</p><div class="card-meta"><span class="who">Owen Pratt</span><svg width="5" height="7" viewBox="0 0 5 7"><path d="M2.5 6.5S.5 4.3.5 2.6a2 2 0 0 1 4 0c0 1.7-2 3.9-2 3.9z" fill="none" stroke="#444" stroke-width=".6"/><circle cx="2.5" cy="2.6" r=".7" fill="#444"/></svg><span class="where">London</span><svg width="7" height="7" viewBox="0 0 7 7"><rect x=".5" y="1" width="6" height="5.5" fill="none" stroke="#444" stroke-width=".6"/><path d="M.5 2.6h6M2 .3v1.4M5 .3v1.4" stroke="#444" stroke-width=".6"/></svg><span>April 2, 2024</span></div></article>
      <article class="card"><div class="avatar av-tan" role="img" aria-label="Colleague portrait photo"></div><h2 class="card-title">Good Quality</h2><div class="stars">★★★★★</div><p class="card-text">Lorem ipsum dolor sit amet, consectetur adipiscing elit, sed do eiusmod tempor incididunt ut labore et dolore magna aliqua. Ut enim ad minim veniam, quis nostrud exercitation ullamco laboris nisi ut aliquip ex ea commodo consequat. Duis aute irure dolor in reprehenderit in voluptate velit esse cillum dolore eu fugiat nulla pariatur. Excepteur sint occaecat cupidatat non proident, sunt in culpa qui officia deserunt mollit anim id est laborum</p><div class="card-meta"><span class="who">Owen Pratt</span><svg width="5" height="7" viewBox="0 0 5 7"><path d="M2.5 6.5S.5 4.3.5 2.6a2 2 0 0 1 4 0c0 1.7-2 3.9-2 3.9z" fill="none" stroke="#444" stroke-width=".6"/><circle cx="2.5" cy="2.6" r=".7" fill="#444"/></svg><span class="where">London</span><svg width="7" height="7" viewBox="0 0 7 7"><rect x=".5" y="1" width="6" height="5.5" fill="none" stroke="#444" stroke-width=".6"/><path d="M.5 2.6h6M2 .3v1.4M5 .3v1.4" stroke="#444" stroke-width=".6"/></svg><span>April 2, 2024</span></div></article>
      <article class="card"><div class="avatar av-grey" role="img" aria-label="Colleague portrait photo"></div><h2 class="card-title">Poor</h2><div class="stars"><span class="off">★★★★★</span></div><p class="card-text">Lorem ipsum dolor sit amet, consectetur adipiscing elit, sed do eiusmod tempor incididunt ut labore et dolore magna aliqua. Ut enim ad minim veniam, quis nostrud exercitation ullamco laboris nisi ut aliquip ex ea commodo consequat. Duis aute irure dolor in reprehenderit in voluptate velit esse cillum dolore eu fugiat nulla pariatur. Excepteur sint occaecat cupidatat non proident, sunt in culpa qui officia deserunt mollit anim id est laborum</p><div class="card-meta"><span class="who">Owen Pratt</span><svg width="5" height="7" viewBox="0 0 5 7"><path d="M2.5 6.5S.5 4.3.5 2.6a2 2 0 0 1 4 0c0 1.7-2 3.9-2 3.9z" fill="none" stroke="#444" stroke-width=".6"/><circle cx="2.5" cy="2.6" r=".7" fill="#444"/></svg><span class="where">London</span><svg width="7" height="7" viewBox="0 0 7 7"><rect x=".5" y="1" width="6" height="5.5" fill="none" stroke="#444" stroke-width=".6"/><path d="M.5 2.6h6M2 .3v1.4M5 .3v1.4" stroke="#444" stroke-width=".6"/></svg><span>April 2, 2024</span></div></article>
      <article class="card"><div class="avatar av-maroon" role="img" aria-label="Colleague portrait photo"></div><h2 class="card-title">Outstanding Performance</h2><div class="stars">★★★★★</div><p class="card-text">Lorem ipsum dolor sit amet, consectetur adipiscing elit, sed do eiusmod tempor incididunt ut labore et dolore magna aliqua. Ut enim ad minim veniam, quis nostrud exercitation ullamco laboris nisi ut aliquip ex ea commodo consequat. Duis aute irure dolor in reprehenderit in voluptate velit esse cillum dolore eu fugiat nulla pariatur. Excepteur sint occaecat cupidatat non proident, sunt in culpa qui officia deserunt mollit anim id est laborum</p><div class="card-meta"><span class="who">Owen Pratt</span><svg width="5" height="7" viewBox="0 0 5 7"><path d="M2.5 6.5S.5 4.3.5 2.6a2 2 0 0 1 4 0c0 1.7-2 3.9-2 3.9z" fill="none" stroke="#444" stroke-width=".6"/><circle cx="2.5" cy="2.6" r=".7" fill="#444"/></svg><span class="where">London</span><svg width="7" height="7" viewBox="0 0 7 7"><rect x=".5" y="1" width="6" height="5.5" fill="none" stroke="#444" stroke-width=".6"/><path d="M.5 2.6h6M2 .3v1.4M5 .3v1.4" stroke="#444" stroke-width=".6"/></svg><span>April 2, 2024</span></div></article>
      <article class="card"><div class="avatar av-slate" role="img" aria-label="Colleague portrait photo"></div><h2 class="card-title">High-Quality Work</h2><div class="stars">★★★★★</div><p class="card-text">Lorem ipsum dolor sit amet, consectetur adipiscing elit, sed do eiusmod tempor incididunt ut labore et dolore magna aliqua. Ut enim ad minim veniam, quis nostrud exercitation ullamco laboris nisi ut aliquip ex ea commodo consequat. Duis aute irure dolor in reprehenderit in voluptate velit esse cillum dolore eu fugiat nulla pariatur. Excepteur sint occaecat cupidatat non proident, sunt in culpa qui officia deserunt mollit anim id est laborum</p><div class="card-meta"><span class="who">Owen Pratt</span><svg width="5" height="7" viewBox="0 0 5 7"><path d="M2.5 6.5S.5 4.3.5 2.6a2 2 0 0 1 4 0c0 1.7-2 3.9-2 3.9z" fill="none" stroke="#444" stroke-width=".6"/><circle cx="2.5" cy="2.6" r=".7" fill="#444"/></svg><span class="where">London</span><svg width="7" height="7" viewBox="0 0 7 7"><rect x=".5" y="1" width="6" height="5.5" fill="none" stroke="#444" stroke-width=".6"/><path d="M.5 2.6h6M2 .3v1.4M5 .3v1.4" stroke="#444" stroke-width=".6"/></svg><span>April 2, 2024</span></div></article>
      <article class="card"><div class="avatar av-sky" role="img" aria-label="Colleague portrait photo"></div><h2 class="card-title">Needs Improvement</h2><div class="stars">★★★<span class="off">★★</span></div><p class="card-text">Lorem ipsum dolor sit amet, consectetur adipiscing elit, sed do eiusmod tempor incididunt ut labore et dolore magna aliqua. Ut enim ad minim veniam, quis nostrud exercitation ullamco laboris nisi ut aliquip ex ea commodo consequat. Duis aute irure dolor in reprehenderit in voluptate velit esse cillum dolore eu fugiat nulla pariatur. Excepteur sint occaecat cupidatat non proident, sunt in culpa qui officia deserunt mollit anim id est laborum</p><div class="card-meta"><span class="who">Owen Pratt</span><svg width="5" height="7" viewBox="0 0 5 7"><path d="M2.5 6.5S.5 4.3.5 2.6a2 2 0 0 1 4 0c0 1.7-2 3.9-2 3.9z" fill="none" stroke="#444" stroke-width=".6"/><circle cx="2.5" cy="2.6" r=".7" fill="#444"/></svg><span class="where">London</span><svg width="7" height="7" viewBox="0 0 7 7"><rect x=".5" y="1" width="6" height="5.5" fill="none" stroke="#444" stroke-width=".6"/><path d="M.5 2.6h6M2 .3v1.4M5 .3v1.4" stroke="#444" stroke-width=".6"/></svg><span>April 2, 2024</span></div></article>
    </div>
    <div class="pager" style="left:252px;top:1579px">
      <span class="arrow"><svg width="5" height="9" viewBox="0 0 5 9"><path d="M4.5.5 .5 4.5l4 4" fill="none" stroke="#999"/></svg></span>
      <span class="page page-on">1</span><span class="page">2</span><span class="page">3</span><span class="page">4</span><span class="page">5</span>
      <span class="arrow"><svg width="5" height="9" viewBox="0 0 5 9"><path d="M.5.5l4 4-4 4" fill="none" stroke="#999"/></svg></span>
    </div>
  </section>

  <!-- Feedback list with request menu open -->
  <section class="screen screen-list-b">
    <header class="screen-head">
      <h1 class="page-title" style="top:21px">LIST OF FEEDBACKS</h1>
      <a class="btn btn-solid" style="left:350px;top:20px;width:108px">Request Feedback<span class="btn-caret"></span></a>
      <a class="btn" style="left:468px;top:20px">Respond to Feedback</a>
      <nav class="request-menu">
        <span class="menu-active" style="width:93px">Adhoc Feedback</span>
        <span style="width:100px">Mid Year Feedback</span>
        <span style="width:83px">360 Feedback</span>
      </nav>
    </header>
    <div class="toolbar" style="top:112px">
      <span class="sort-label">Sort By</span>
      <span class="select" style="left:109px;width:47px">Newest<svg width="6" height="4" viewBox="0 0 6 4"><path d="M.5.5 3 3 5.5.5" fill="none" stroke="#444" stroke-width=".8"/></svg></span>
      <span class="select" style="left:162px;width:58px">Date Range<svg width="6" height="4" viewBox="0 0 6 4"><path d="M.5.5 3 3 5.5.5" fill="none" stroke="#444" stroke-width=".8"/></svg></span>
      <span class="select" style="left:226px;width:57px">Very Good<svg width="6" height="4" viewBox="0 0 6 4"><path d="M.5.5 3 3 5.5.5" fill="none" stroke="#444" stroke-width=".8"/></svg></span>
      <div class="pager" style="left:439px;top:2px">
        <span class="arrow"><svg width="5" height="9" viewBox="0 0 5 9"><path d="M4.5.5 .5 4.5l4 4" fill="none" stroke="#999"/></svg></span>
        <span class="page page-on">1</span><span class="page">2</span><span class="page">3</span><span class="page">4</span><span class="page">5</span>
        <span class="arrow"><svg width="5" height="9" viewBox="0 0 5 9"><path d="M.5.5l4 4-4 4" fill="none" stroke="#999"/></svg></span>
      </div>
    </div>
    <div class="feed" style="top:151px">
      <article class="card"><div class="avatar av-tan" role="img" aria-label="Colleague portrait photo"></div><h2 class="card-title">Good Quality</h2><div class="stars">★★★★★</div><p class="card-text">Lorem ipsum dolor sit amet, consectetur adipiscing elit, sed do eiusmod tempor incididunt ut labore et dolore magna aliqua. Ut enim ad minim veniam, quis nostrud exercitation ullamco laboris nisi ut aliquip ex ea commodo consequat. Duis aute irure dolor in reprehenderit in voluptate velit esse cillum dolore eu fugiat nulla pariatur. Excepteur sint occaecat cupidatat non proident, sunt in culpa qui officia deserunt mollit anim id est laborum</p><div class="card-meta"><span class="who">Owen Pratt</span><svg width="5" height="7" viewBox="0 0 5 7"><path d="M2.5 6.5S.5 4.3.5 2.6a2 2 0 0 1 4 0c0 1.7-2 3.9-2 3.9z" fill="none" stroke="#444" stroke-width=".6"/><circle cx="2.5" cy="2.6" r=".7" fill="#444"/></svg><span class="where">London</span><svg width="7" height="7" viewBox="0 0 7 7"><rect x=".5" y="1" width="6" height="5.5" fill="none" stroke="#444" stroke-width=".6"/><path d="M.5 2.6h6M2 .3v1.4M5 .3v1.4" stroke="#444" stroke-width=".6"/></svg><span>April 2, 2024</span></div></article>
      <article class="card"><div class="avatar av-grey" role="img" aria-label="Colleague portrait photo"></div><h2 class="card-title">Poor</h2><div class="stars"><span class="off">★★★★★</span></div><p class="card-text">Lorem ipsum dolor sit amet, consectetur adipiscing elit, sed do eiusmod tempor incididunt ut labore et dolore magna aliqua. Ut enim ad minim veniam, quis nostrud exercitation ullamco laboris nisi ut aliquip ex ea commodo consequat. Duis aute irure dolor in reprehenderit in voluptate velit esse cillum dolore eu fugiat nulla pariatur. Excepteur sint occaecat cupidatat non proident, sunt in culpa qui officia deserunt mollit anim id est laborum</p><div class="card-meta"><span class="who">Owen Pratt</span><svg width="5" height="7" viewBox="0 0 5 7"><path d="M2.5 6.5S.5 4.3.5 2.6a2 2 0 0 1 4 0c0 1.7-2 3.9-2 3.9z" fill="none" stroke="#444" stroke-width=".6"/><circle cx="2.5" cy="2.6" r=".7" fill="#444"/></svg><span class="where">London</span><svg width="7" height="7" viewBox="0 0 7 7"><rect x=".5" y="1" width="6" height="5.5" fill="none" stroke="#444" stroke-width=".6"/><path d="M.5 2.6h6M2 .3v1.4M5 .3v1.4" stroke="#444" stroke-width=".6"/></svg><span>April 2, 2024</span></div></article>
      <article class="card"><div class="avatar av-maroon" role="img" aria-label="Colleague portrait photo"></div><h2 class="card-title">Outstanding Performance</h2><div class="stars">★★★★★</div><p class="card-text">Lorem ipsum dolor sit amet, consectetur adipiscing elit, sed do eiusmod tempor incididunt ut labore et dolore magna aliqua. Ut enim ad minim veniam, quis nostrud exercitation ullamco laboris nisi ut aliquip ex ea commodo consequat. Duis aute irure dolor in reprehenderit in voluptate velit esse cillum dolore eu fugiat nulla pariatur. Excepteur sint occaecat cupidatat non proident, sunt in culpa qui officia deserunt mollit anim id est laborum</p><div class="card-meta"><span class="who">Owen Pratt</span><svg width="5" height="7" viewBox="0 0 5 7"><path d="M2.5 6.5S.5 4.3.5 2.6a2 2 0 0 1 4 0c0 1.7-2 3.9-2 3.9z" fill="none" stroke="#444" stroke-width=".6"/><circle cx="2.5" cy="2.6" r=".7" fill="#444"/></svg><span class="where">London</span><svg width="7" height="7" viewBox="0 0 7 7"><rect x=".5" y="1" width="6" height="5.5" fill="none" stroke="#444" stroke-width=".6"/><path d="M.5 2.6h6M2 .3v1.4M5 .3v1.4" stroke="#444" stroke-width=".6"/></svg><span>April 2, 2024</span></div></article>
      <article class="card"><div class="avatar av-slate" role="img" aria-label="Colleague portrait photo"></div><h2 class="card-title">High-Quality Work</h2><div class="stars">★★★★★</div><p class="card-text">Lorem ipsum dolor sit amet, consectetur adipiscing elit, sed do eiusmod tempor incididunt ut labore et dolore magna aliqua. Ut enim ad minim veniam, quis nostrud exercitation ullamco laboris nisi ut aliquip ex ea commodo consequat. Duis aute irure dolor in reprehenderit in voluptate velit esse cillum dolore eu fugiat nulla pariatur. Excepteur sint occaecat cupidatat non proident, sunt in culpa qui officia deserunt mollit anim id est laborum</p><div class="card-meta"><span class="who">Owen Pratt</span><svg width="5" height="7" viewBox="0 0 5 7"><path d="M2.5 6.5S.5 4.3.5 2.6a2 2 0 0 1 4 0c0 1.7-2 3.9-2 3.9z" fill="none" stroke="#444" stroke-width=".6"/><circle cx="2.5" cy="2.6" r=".7" fill="#444"/></svg><span class="where">London</span><svg width="7" height="7" viewBox="0 0 7 7"><rect x=".5" y="1" width="6" height="5.5" fill="none" stroke="#444" stroke-width=".6"/><path d="M.5 2.6h6M2 .3v1.4M5 .3v1.4" stroke="#444" stroke-width=".6"/></svg><span>April 2, 2024</span></div></article>
      <article class="card"><div class="avatar av-sky" role="img" aria-label="Colleague portrait photo"></div><h2 class="card-title">Needs Improvement</h2><div class="stars">★★★<span class="off">★★</span></div><p class="card-text">Lorem ipsum dolor sit amet, consectetur adipiscing elit, sed do eiusmod tempor incididunt ut labore et dolore magna aliqua. Ut enim ad minim veniam, quis nostrud exercitation ullamco laboris nisi ut aliquip ex ea commodo consequat. Duis aute irure dolor in reprehenderit in voluptate velit esse cillum dolore eu fugiat nulla pariatur. Excepteur sint occaecat cupidatat non proident, sunt in culpa qui officia deserunt mollit anim id est laborum</p><div class="card-meta"><span class="who">Owen Pratt</span><svg width="5" height="7" viewBox="0 0 5 7"><path d="M2.5 6.5S.5 4.3.5 2.6a2 2 0 0 1 4 0c0 1.7-2 3.9-2 3.9z" fill="none" stroke="#444" stroke-width=".6"/><circle cx="2.5" cy="2.6" r=".7" fill="#444"/></svg><span class="where">London</span><svg width="7" height="7" viewBox="0 0 7 7"><rect x=".5" y="1" width="6" height="5.5" fill="none" stroke="#444" stroke-width=".6"/><path d="M.5 2.6h6M2 .3v1.4M5 .3v1.4" stroke="#444" stroke-width=".6"/></svg><span>April 2, 2024</span></div></article>
      <article class="card"><div class="avatar av-tan" role="img" aria-label="Colleague portrait photo"></div><h2 class="card-title">Good Quality</h2><div class="stars">★★★★★</div><p class="card-text">Lorem ipsum dolor sit amet, consectetur adipiscing elit, sed do eiusmod tempor incididunt ut labore et dolore magna aliqua. Ut enim ad minim veniam, quis nostrud exercitation ullamco laboris nisi ut aliquip ex ea commodo consequat. Duis aute irure dolor in reprehenderit in voluptate velit esse cillum dolore eu fugiat nulla pariatur. Excepteur sint occaecat cupidatat non proident, sunt in culpa qui officia deserunt mollit anim id est laborum</p><div class="card-meta"><span class="who">Owen Pratt</span><svg width="5" height="7" viewBox="0 0 5 7"><path d="M2.5 6.5S.5 4.3.5 2.6a2 2 0 0 1 4 0c0 1.7-2 3.9-2 3.9z" fill="none" stroke="#444" stroke-width=".6"/><circle cx="2.5" cy="2.6" r=".7" fill="#444"/></svg><span class="where">London</span><svg width="7" height="7" viewBox="0 0 7 7"><rect x=".5" y="1" width="6" height="5.5" fill="none" stroke="#444" stroke-width=".6"/><path d="M.5 2.6h6M2 .3v1.4M5 .3v1.4" stroke="#444" stroke-width=".6"/></svg><span>April 2, 2024</span></div></article>
      <article class="card"><div class="avatar av-grey" role="img" aria-label="Colleague portrait photo"></div><h2 class="card-title">Poor</h2><div class="stars"><span class="off">★★★★★</span></div><p class="card-text">Lorem ipsum dolor sit amet, consectetur adipiscing elit, sed do eiusmod tempor incididunt ut labore et dolore magna aliqua. Ut enim ad minim veniam, quis nostrud exercitation ullamco laboris nisi ut aliquip ex ea commodo consequat. Duis aute irure dolor in reprehenderit in voluptate velit esse cillum dolore eu fugiat nulla pariatur. Excepteur sint occaecat cupidatat non proident, sunt in culpa qui officia deserunt mollit anim id est laborum</p><div class="card-meta"><span class="who">Owen Pratt</span><svg width="5" height="7" viewBox="0 0 5 7"><path d="M2.5 6.5S.5 4.3.5 2.6a2 2 0 0 1 4 0c0 1.7-2 3.9-2 3.9z" fill="none" stroke="#444" stroke-width=".6"/><circle cx="2.5" cy="2.6" r=".7" fill="#444"/></svg><span class="where">London</span><svg width="7" height="7" viewBox="0 0 7 7"><rect x=".5" y="1" width="6" height="5.5" fill="none" stroke="#444" stroke-width=".6"/><path d="M.5 2.6h6M2 .3v1.4M5 .3v1.4" stroke="#444" stroke-width=".6"/></svg><span>April 2, 2024</span></div></article>
      <article class="card"><div class="avatar av-maroon" role="img" aria-label="Colleague portrait photo"></div><h2 class="card-title">Outstanding Performance</h2><div class="stars">★★★★★</div><p class="card-text">Lorem ipsum dolor sit amet, consectetur adipiscing elit, sed do eiusmod tempor incididunt ut labore et dolore magna aliqua. Ut enim ad minim veniam, quis nostrud exercitation ullamco laboris nisi ut aliquip ex ea commodo consequat. Duis aute irure dolor in reprehenderit in voluptate velit esse cillum dolore eu fugiat nulla pariatur. Excepteur sint occaecat cupidatat non proident, sunt in culpa qui officia deserunt mollit anim id est laborum</p><div class="card-meta"><span class="who">Owen Pratt</span><svg width="5" height="7" viewBox="0 0 5 7"><path d="M2.5 6.5S.5 4.3.5 2.6a2 2 0 0 1 4 0c0 1.7-2 3.9-2 3.9z" fill="none" stroke="#444" stroke-width=".6"/><circle cx="2.5" cy="2.6" r=".7" fill="#444"/></svg><span class="where">London</span><svg width="7" height="7" viewBox="0 0 7 7"><rect x=".5" y="1" width="6" height="5.5" fill="none" stroke="#444" stroke-width=".6"/><path d="M.5 2.6h6M2 .3v1.4M5 .3v1.4" stroke="#444" stroke-width=".6"/></svg><span>April 2, 2024</span></div></article>
      <article class="card"><div class="avatar av-slate" role="img" aria-label="Colleague portrait photo"></div><h2 class="card-title">High-Quality Work</h2><div class="stars">★★★★★</div><p class="card-text">Lorem ipsum dolor sit amet, consectetur adipiscing elit, sed do eiusmod tempor incididunt ut labore et dolore magna aliqua. Ut enim ad minim veniam, quis nostrud exercitation ullamco laboris nisi ut aliquip ex ea commodo consequat. Duis aute irure dolor in reprehenderit in voluptate velit esse cillum dolore eu fugiat nulla pariatur. Excepteur sint occaecat cupidatat non proident, sunt in culpa qui officia deserunt mollit anim id est laborum</p><div class="card-meta"><span class="who">Owen Pratt</span><svg width="5" height="7" viewBox="0 0 5 7"><path d="M2.5 6.5S.5 4.3.5 2.6a2 2 0 0 1 4 0c0 1.7-2 3.9-2 3.9z" fill="none" stroke="#444" stroke-width=".6"/><circle cx="2.5" cy="2.6" r=".7" fill="#444"/></svg><span class="where">London</span><svg width="7" height="7" viewBox="0 0 7 7"><rect x=".5" y="1" width="6" height="5.5" fill="none" stroke="#444" stroke-width=".6"/><path d="M.5 2.6h6M2 .3v1.4M5 .3v1.4" stroke="#444" stroke-width=".6"/></svg><span>April 2, 2024</span></div></article>
      <article class="card"><div class="avatar av-sky" role="img" aria-label="Colleague portrait photo"></div><h2 class="card-title">Needs Improvement</h2><div class="stars">★★★<span class="off">★★</span></div><p class="card-text">Lorem ipsum dolor sit amet, consectetur adipiscing elit, sed do eiusmod tempor incididunt ut labore et dolore magna aliqua. Ut enim ad minim veniam, quis nostrud exercitation ullamco laboris nisi ut aliquip ex ea commodo consequat. Duis aute irure dolor in reprehenderit in voluptate velit esse cillum dolore eu fugiat nulla pariatur. Excepteur sint occaecat cupidatat non proident, sunt in culpa qui officia deserunt mollit anim id est laborum</p><div class="card-meta"><span class="who">Owen Pratt</span><svg width="5" height="7" viewBox="0 0 5 7"><path d="M2.5 6.5S.5 4.3.5 2.6a2 2 0 0 1 4 0c0 1.7-2 3.9-2 3.9z" fill="none" stroke="#444" stroke-width=".6"/><circle cx="2.5" cy="2.6" r=".7" fill="#444"/></svg><span class="where">London</span><svg width="7" height="7" viewBox="0 0 7 7"><rect x=".5" y="1" width="6" height="5.5" fill="none" stroke="#444" stroke-width=".6"/><path d="M.5 2.6h6M2 .3v1.4M5 .3v1.4" stroke="#444" stroke-width=".6"/></svg><span>April 2, 2024</span></div></article>
    </div>
    <div class="pager" style="left:252px;top:1587px">
      <span class="arrow"><svg width="5" height="9" viewBox="0 0 5 9"><path d="M4.5.5 .5 4.5l4 4" fill="none" stroke="#999"/></svg></span>
      <span class="page page-on">1</span><span class="page">2</span><span class="page">3</span><span class="page">4</span><span class="page">5</span>
      <span class="arrow"><svg width="5" height="9" viewBox="0 0 5 9"><path d="M.5.5l4 4-4 4" fill="none" stroke="#999"/></svg></span>
    </div>
  </section>

  <!-- Adhoc feedback request screen -->
  <section class="screen screen-adhoc">
    <header class="screen-head">
      <h1 class="page-title" style="top:20px">ADHOC FEEDBACK</h1>
      <a class="btn btn-solid" style="left:351px;top:20px;width:108px">Request Feedback</a>
      <a class="btn" style="left:469px;top:20px">Respond to Feedback</a>
    </header>
    <label class="search">Search colleagues<svg width="9" height="9" viewBox="0 0 9 9"><circle cx="3.8" cy="3.8" r="3" fill="none" stroke="#999" stroke-width=".8"/><path d="M6 6l2.5 2.5" stroke="#999" stroke-width=".8"/></svg></label>
    <div class="people">
      <div class="person person-first" style="top:0">
        <div class="avatar av-grey" role="img" aria-label="Colleague portrait photo"></div>
        <span class="picked"><svg width="7" height="7" viewBox="0 0 7 7" style="position:absolute;left:0;top:0"><path d="M1.6 3.6 3 4.9 5.4 2.2" fill="none" stroke="#fff" stroke-width="1"/></svg></span>
        <span class="person-name">Daniel R. Hale</span>
        <span class="person-btn">Request Feedback</span>
        <div class="questions">
          <p>In what areas do you believe I excel, and why?<svg width="7" height="7" viewBox="0 0 7 7"><path d="M3 1H.5v5.5H6V4" fill="none" stroke="#333" stroke-width=".6"/><path d="M2.6 4.4 2.8 3.4 5.6.6l.8.8-2.8 2.8z" fill="none" stroke="#333" stroke-width=".6"/></svg></p>
          <p>What specific actions or behaviors could I improve upon to enhance my performance?<svg width="7" height="7" viewBox="0 0 7 7"><path d="M3 1H.5v5.5H6V4" fill="none" stroke="#333" stroke-width=".6"/><path d="M2.6 4.4 2.8 3.4 5.6.6l.8.8-2.8 2.8z" fill="none" stroke="#333" stroke-width=".6"/></svg></p>
          <p>How can I better support you or contribute to our team's success in the future?<svg width="7" height="7" viewBox="0 0 7 7"><path d="M3 1H.5v5.5H6V4" fill="none" stroke="#333" stroke-width=".6"/><path d="M2.6 4.4 2.8 3.4 5.6.6l.8.8-2.8 2.8z" fill="none" stroke="#333" stroke-width=".6"/></svg></p>
        </div>
      </div>
      <div class="person" style="top:114px;border-top:0"><div class="avatar av-slate" role="img" aria-label="Colleague portrait photo"></div><span class="person-name">Peter L. Crane</span><span class="person-btn">Request Feedback</span></div>
      <div class="person" style="top:158px"><div class="avatar av-tan" role="img" aria-label="Colleague portrait photo"></div><span class="person-name">Victor T. Marsh</span><span class="person-btn">Request Feedback</span></div>
      <div class="person" style="top:202px"><div class="avatar av-sky" role="img" aria-label="Colleague portrait photo"></div><span class="person-name">Aaron K. Lowell</span><span class="person-btn">Request Feedback</span></div>
      <div class="person" style="top:247px"><div class="avatar av-slate" role="img" aria-label="Colleague portrait photo"></div><span class="person-name">Colin J. Reeve</span><span class="person-btn">Request Feedback</span></div>
      <div class="person" style="top:291px"><div class="avatar av-tan" role="img" aria-label="Colleague portrait photo"></div><span class="person-name">Graham P. Ashby</span><span class="person-btn">Request Feedback</span></div>
      <div class="person" style="top:334px"><div class="avatar av-grey" role="img" aria-label="Colleague portrait photo"></div><span class="person-name">Whitcombe</span><span class="person-btn">Request Feedback</span></div>
      <div class="person" style="top:378px"><div class="avatar av-grey" role="img" aria-label="Colleague portrait photo"></div><span class="person-name">Neil S. Burke</span><span class="person-btn">Request Feedback</span></div>
      <div class="person" style="top:424px"><div class="avatar av-slate" role="img" aria-label="Colleague portrait photo"></div><span class="person-name">Simon A. Vale</span><span class="person-btn">Request Feedback</span></div>
      <div class="person" style="top:469px"><div class="avatar av-sky" role="img" aria-label="Colleague portrait photo"></div><span class="person-name">Ross E. Tate</span><span class="person-btn">Request Feedback</span></div>
    </div>
  </section>

</div>
</body>
</html>
```